Thornfield Marsh, LLC Website

We are a small law firm in need of a website that contains the following:
1. Attractive main page
2. About us/attorney info for three people: Leonard Thornfield (attorney), Brent Marsh (attorney), and Melinda Carrow (legal assistant). We have bio's ready to submit.
3. Blog/video page. We'd like to post blogs and videos to help drive traffic
4. Multidistrict Litigation and Class Actions page, where we post information regarding active MDLs and Class actions that we are doing intake on.
Updates

Can you also please use the color "gold" in the design and logo? Thanks.

Industry/Entity Type

Legal

Coding

Coded - Design and coding required

Number of Pages Required

1 page

Colors
0054AA
0677BA
7BADD7
CADEEF
E8F1F8

Requirements
Must have
• 1. Attractive main page 2. About us/attorney info for three people: Leonard Thornfield (attorney), Brent Marsh (attorney), and Melinda Carrow (legal assistant). We have bio's ready to submit. 3. Blog/video page. We'd like to post blogs and videos to help drive traffic 4. Multidistrict Litigation and Class Actions page, where we post information regarding active MDLs and Class actions that we are doing intake on.

```html
<!DOCTYPE html>
<html lang="en">
<head>
<meta charset="utf-8">
<title>Thornfield Marsh, LLC</title>
<link href="https://fonts.googleapis.com/css2?family=Montserrat:wght@400;500;600;700;800&display=swap" rel="stylesheet">
<style>
:root{
  --navy:#262e86;
  --navy-dark:#1d2470;
  --gold:#d4a11b;
  --sky:#4ba9e1;
  --ink:#1f2450;
  --grey-bg:#eeeff3;
  --pale:#e8f1f8;
  --white:#ffffff;
}
*{margin:0;padding:0;box-sizing:border-box}
html,body{width:1200px;height:5333px;overflow:hidden}
body{font-family:"Montserrat",sans-serif;color:var(--ink);background:var(--white);position:relative}
section,header,footer{position:absolute;left:0;width:1200px;overflow:hidden}
.abs{position:absolute}
.photo{position:absolute}
.brand{display:flex;align-items:center;gap:8px;font-weight:700;font-size:14px;color:var(--navy);letter-spacing:.3px;white-space:nowrap}
.brand-mark{width:20px;height:20px;background:var(--gold)}
.label{font-size:15px;letter-spacing:3px;color:var(--ink);font-weight:500}
.heading{display:flex;align-items:center;font-size:33px;font-weight:700;letter-spacing:.5px}
.heading span{white-space:nowrap}
.heading .light{color:var(--sky);margin-right:8px;font-weight:600}
.heading .boxed{background:var(--navy);color:var(--white);padding:2px 12px}
.btn{display:inline-block;background:var(--gold);color:var(--white);font-weight:600;font-size:14px;letter-spacing:1px;padding:13px 32px}
p{line-height:1.5}

/* header */
.site-header{top:0;height:80px;z-index:5}
.site-header .brand{position:absolute;left:95px;top:22px;border:2px solid var(--navy);padding:8px 12px;background:var(--white)}
.nav{position:absolute;left:412px;top:34px;display:flex;gap:48px;font-size:13px;font-weight:600;color:var(--ink)}
.nav .active{border-bottom:2px solid var(--sky);padding-bottom:8px}
.phone-box{position:absolute;right:0;top:0;width:192px;height:72px;background:var(--navy);color:var(--white);display:flex;align-items:center;justify-content:center;gap:10px;font-size:15px;font-weight:600}
.phone-box .dot{width:20px;height:20px;border-radius:50%;background:var(--gold)}

/* hero */
.hero{top:0;height:724px;background:linear-gradient(180deg,#f4f4f4 0%,#cfcfcf 35%,#8d8d8d 70%,#5e5e5e 100%)}
.hero-inner{position:absolute;top:125px;left:0;width:1200px;text-align:center}
.hero .mark{width:36px;height:22px;background:var(--gold);margin:0 auto 14px}
.hero .tag{font-size:18px;font-weight:600;letter-spacing:4px;color:var(--navy)}
.hero-title{display:inline-flex;margin-top:14px;border:3px solid var(--navy);font-size:46px;font-weight:700;white-space:nowrap}
.hero-title .a{background:var(--navy);color:var(--white);padding:4px 18px}
.hero-title .b{background:var(--white);color:var(--gold);padding:4px 18px}
.hero p{font-size:18px;color:var(--ink);margin:24px auto 0;width:520px}
.hero .btn{margin-top:24px}

/* about */
.about{top:724px;height:592px;background:var(--white)}
.about-text{left:645px;top:86px;width:480px}
.about-text .heading{margin-top:10px;font-size:30px}
.about-text p{font-size:13px;margin-top:24px;line-height:1.55}
.about-text .btn{margin-top:28px;padding:12px 32px}

/* attorneys */
.meet{top:1316px;height:666px;background:var(--grey-bg)}
.meet-head{left:0;top:65px;width:1200px;text-align:center}
.meet-head .mark{width:36px;height:20px;background:var(--sky);margin:0 auto 6px}
.meet-head .heading{justify-content:center;margin-top:4px}
.bio{position:absolute}
.bio .name{font-size:32px;font-weight:700;color:var(--navy);border-left:3px solid var(--sky);padding-left:12px;line-height:1.1}
.bio .role{font-size:14px;font-weight:600;color:var(--sky);border-left:3px solid var(--sky);padding-left:12px;padding-top:8px;letter-spacing:.5px}
.bio p{font-size:16px;margin-top:22px}
.lead .bio{left:118px;top:216px;width:570px}

.second{top:1982px;height:563px;background:var(--sky)}
.second .bio{left:568px;top:100px;width:540px}
.second .bio .name,.second .bio .role,.second .bio p{color:var(--white);border-color:var(--white)}

.third{top:2545px;height:631px;background:linear-gradient(90deg,#ffffff 0%,#f3f4f8 100%)}
.third .bio{left:133px;top:115px;width:530px}
.third .bio p{font-size:15.5px}

/* blogs */
.blogs{top:3176px;height:662px;background:var(--white)}
.blogs-head{left:116px;top:70px}
.blogs-head .heading{margin-top:8px}
.blog-main{left:116px;top:169px;width:481px;height:395px;background:linear-gradient(160deg,#9aa0b0,#4b5165)}
.blog-main .cap{position:absolute;left:0;bottom:0;width:100%;height:98px;background:rgba(38,46,134,.88);color:var(--white);padding:18px 32px}
.blog-main .cap h3{font-size:16px;font-weight:700}
.blog-main .cap p{font-size:12px;margin-top:6px;line-height:1.3}
.play{position:absolute;left:206px;top:95px;width:66px;height:66px;border-radius:50%;background:rgba(255,255,255,.3);border:2px solid var(--white)}
.blog-card{position:absolute;left:610px;width:512px;height:188px;border:1px solid #c5c8e0;display:flex;background:var(--white)}
.blog-card .thumb{width:246px;height:100%;background:linear-gradient(150deg,#b5b9c4,#5e6374)}
.blog-card .txt{padding:30px 18px 0 20px;flex:1}
.date{display:inline-block;background:var(--gold);color:var(--white);font-size:10px;font-weight:700;padding:5px 10px}
.blog-card h4{font-size:14px;color:var(--navy);font-weight:600;margin-top:8px;line-height:1.25}
.blog-card p{font-size:10px;color:#666;margin-top:8px;line-height:1.45}
.dots{left:536px;top:3782px;display:flex;gap:14px}
.dots span{width:38px;height:3px;background:var(--sky)}
.dots span.on{background:var(--navy)}

/* MDL */
.mdl{top:3838px;height:631px;background:linear-gradient(90deg,#dbe6f3 0%,#f1f5fb 60%,#ffffff 100%)}
.mdl-text{left:617px;top:127px;width:540px}
.mdl-text .heading{font-size:32px;flex-wrap:wrap;line-height:1.3}
.mdl-text .h1{color:var(--sky);font-weight:600;width:100%}
.mdl-text p{font-size:16px;margin-top:24px}

/* contact */
.contact{top:4469px;height:621px;background:var(--navy)}
.contact-text{left:116px;top:131px;width:460px;color:var(--white)}
.contact-text .label{color:var(--white)}
.contact-text .heading{color:var(--white);margin-top:8px}
.contact-text .heading .boxed{background:var(--sky)}
.contact-text .intro{font-size:15px;margin-top:26px;line-height:1.4}
.info{display:flex;gap:14px;margin-top:24px;font-size:19px;line-height:1.3}
.info svg{flex:none;margin-top:2px}
.form{left:595px;top:106px;width:545px;height:385px;background:var(--gold);padding:46px 54px}
.frame{position:absolute;border:2px solid #5b63b0}
.row{display:flex;gap:10px;margin-bottom:12px}
.field{flex:1;height:46px;background:var(--white);font-size:13px;color:var(--ink);display:flex;align-items:center;padding-left:22px;gap:8px}
.field.tall{height:112px;align-items:flex-start;padding-top:16px}
.field i{width:10px;height:10px;background:#9aa0c5;display:inline-block;border-radius:2px}
.send{display:inline-block;background:var(--navy);color:var(--white);font-size:12px;font-weight:700;letter-spacing:.5px;padding:14px 40px}

/* footer */
.site-footer{top:5090px;height:243px;background:var(--white)}
.site-footer .brand{position:absolute;left:120px;top:48px;border:2px solid var(--navy);padding:8px 12px}
.fnav{position:absolute;left:467px;top:62px;display:flex;gap:68px;font-size:15px;font-weight:600;color:var(--navy)}
.rule{position:absolute;left:0;top:133px;width:1200px;height:1px;background:#dfe1ea}
.copy{position:absolute;left:116px;top:168px;font-size:14px;color:var(--ink)}
.social{position:absolute;left:938px;top:158px;display:flex;gap:8px}
.social span{width:36px;height:36px;border-radius:50%;background:var(--navy)}
.social span:nth-child(2){background:var(--sky)}
.social span:nth-child(3){background:#4f96d6}
</style>
</head>
<body>

<section class="hero">
  <div class="photo" role="img" aria-label="Black and white aerial photograph of the downtown city skyline" style="inset:0;background:linear-gradient(180deg,rgba(255,255,255,.65) 0%,rgba(255,255,255,.2) 40%,rgba(40,40,40,.15) 100%)"></div>
  <div class="hero-inner">
    <div class="mark"></div>
    <div class="tag">— A MULTI-SERVICE LAW FIRM —</div>
    <div class="hero-title"><span class="a">THORNFIELD MARSH</span><span class="b">LLC LAWYERS</span></div>
    <p>Thornfield, Marsh, and Ashby LLC is a multi-service law firm located in downtown Mobile, Alabama.</p>
    <span class="btn">SCHEDULE CONSULTATION ›</span>
  </div>
</section>

<header class="site-header">
  <div class="brand"><span class="brand-mark"></span>THORNFIELD MARSH LLC</div>
  <nav class="nav"><span class="active">HOME</span><span>ABOUT US</span><span>BLOGS</span><span>MDLS AND CLASS ACTIONS</span></nav>
  <div class="phone-box"><span class="dot"></span>(555) 014-2270</div>
</header>

<section class="about">
  <svg class="abs" style="left:0;top:0" width="620" height="592" viewBox="0 0 620 592">
    <polygon points="0,0 615,0 440,592 0,592" fill="#8a8a8a"/>
    <line x1="640" y1="0" x2="460" y2="530" stroke="#d4a11b" stroke-width="5"/>
  </svg>
  <div class="photo" role="img" aria-label="Black and white photograph of two business people shaking hands across a desk" style="left:0;top:0;width:615px;height:592px;clip-path:polygon(0 0,100% 0,71.5% 100%,0 100%);background:linear-gradient(135deg,#c9c9c9,#555)"></div>
  <div class="abs" style="left:490px;top:298px;width:96px;height:96px;border-radius:50%;background:var(--white)"></div>
  <div class="abs about-text">
    <div class="label">OUR LAW FIRM</div>
    <div class="heading"><span class="light">ABOUT</span><span class="boxed">THORNFIELD MARSH</span></div>
    <p>Thornfield, Marsh, and Ashby LLC is a multi-service law firm located in downtown Mobile, Alabama. Our Mobile business litigation lawyers are licensed to practice law in the following Gulf Coast states: Alabama and Florida. We handle a variety of legal issues facing individuals and businesses, including: insurance claims, minimum and overtime pay issues under the Wage and Hour laws, employment law, workers compensation, Medicare fraud, collections, mediation, arbitration, and general civil litigation.</p>
    <p style="margin-top:16px">Our Mobile business litigation attorneys pride ourselves on being accessible to our clients and providing exceptional value for the legal services rendered. We strive to serve our clients</p>
    <span class="btn">LEARN MORE ›</span>
  </div>
  <div class="abs" style="left:599px;top:558px;width:2px;height:34px;background:var(--navy)"></div>
</section>

<section class="meet lead">
  <div class="abs" style="left:599px;top:0;width:2px;height:36px;background:var(--navy)"></div>
  <div class="abs" style="left:594px;top:34px;width:12px;height:12px;border-radius:50%;background:var(--navy)"></div>
  <div class="photo" role="img" aria-label="Blue toned photograph of classical courthouse columns" style="left:0;top:0;width:1200px;height:666px;clip-path:polygon(1030px 0,1200px 0,1200px 666px,800px 666px);background:linear-gradient(160deg,#3c46a8,#262e86)"></div>
  <div class="abs meet-head">
    <div class="mark"></div>
    <div class="label">OUR ATTORNEY</div>
    <div class="heading"><span class="light">MEET OUR</span><span class="boxed">ATTORNEY</span></div>
  </div>
  <div class="bio">
    <div class="name">LEONARD THORNFIELD</div>
    <div class="role">PARTNER</div>
    <p>Leonard Thornfield has practiced in our local court system for nearly 20 years. He is regularly appointed as a mediator and guardian ad litem.</p>
    <p>In his private practice, Leonard helps businesses and people that face legal challenges, including:</p>
    <p>Construction: Representation of general contractors, subcontractors, and material suppliers regarding contract negotiations, collections, general litigation, insurance coverage opinions and disputes, and misc. legal issues;</p>
  </div>
  <div class="photo" role="img" aria-label="Portrait photograph of the partner in a dark suit" style="left:715px;top:184px;width:380px;height:482px;background:linear-gradient(180deg,#d0d0d0,#3a3a3a);border-radius:150px 150px 0 0"></div>
</section>

<section class="second">
  <div class="abs" style="left:0;top:0;width:1200px;height:563px;background:var(--gold);clip-path:polygon(0 0,465px 0,265px 563px,0 563px)"></div>
  <div class="photo" role="img" aria-label="Portrait photograph of the attorney in a grey suit and striped tie" style="left:108px;top:62px;width:410px;height:501px;background:linear-gradient(180deg,#dedede,#6a6a6a);border-radius:150px 150px 0 0"></div>
  <div class="bio">
    <div class="name">BRENT MARSH</div>
    <div class="role">ATTORNEY</div>
    <p>Brent Marsh helps people reclaim their voices and protect their rights, providing consumer debt defense, criminal defense, and insurance litigation. Sued by a Credit Card or Loan Company?</p>
    <p>Brent will help you take on major corporations. He has represented over 2000 people in consumer debt cases and negotiations, seeking dismissals with major creditors like Keystone Bank, Meridian National Bank, and Atlas Card Services. Some recent victories include a 65% reduction on a Northgate Funding account, a wage garnishment protection for a Meridian National Bank customer, and a vacated default judgment.</p>
  </div>
</section>

<section class="third">
  <div class="photo" role="img" aria-label="Portrait photograph of the legal assistant over a soft blue city background" style="left:660px;top:0;width:540px;height:631px;background:linear-gradient(90deg,rgba(255,255,255,0) 0%,#c9cde6 40%,#aab1db 100%)"></div>
  <div class="photo" role="img" aria-label="Portrait photograph of a man in a dark suit" style="left:690px;top:48px;width:350px;height:583px;background:linear-gradient(180deg,#cfcfcf,#404040);border-radius:150px 150px 0 0"></div>
  <div class="bio">
    <div class="name">MELINDA CARROW</div>
    <div class="role">LEGAL ASSISTANT</div>
    <p>Lorem ipsum dolor sit amet, consectetur adipiscing elit, sed do eiusmod tempor incididunt ut labore et dolore magna aliqua. Ut enim ad minim veniam, quis nostrud exercitation ullamco laboris nisi ut aliquip ex ea commodo consequat. Duis aute irure dolor in reprehenderit in voluptate velit esse cillum dolore eu fugiat nulla pariatur Excepteur sint occaecat</p>
    <p>Sed ut perspiciatis unde omnis iste natus error sit voluptatem accusantium doloremque laudantium, totam rem aperiam, eaque ipsa quae ab illo inventore veritatis et quasi architecto beatae vitae dicta sunt explicabo. vatem quia volu</p>
  </div>
</section>

<section class="blogs">
  <div class="abs" style="left:0;top:110px;width:70px;height:2px;background:var(--sky)"></div>
  <div class="abs" style="left:66px;top:106px;width:10px;height:10px;border-radius:50%;background:var(--sky)"></div>
  <div class="abs blogs-head">
    <div class="label">OUR ATTORNEY</div>
    <div class="heading"><span class="light">LATEST</span><span class="boxed">BLOGS</span></div>
  </div>
  <div class="abs blog-main" role="img" aria-label="Video still of two people reviewing documents at a desk">
    <div class="play"></div>
    <svg class="abs" style="left:232px;top:118px" width="20" height="22" viewBox="0 0 20 22"><polygon points="2,1 19,11 2,21" fill="#fff"/></svg>
    <div class="cap">
      <h3>Lorem ipsum dolor sit amet consectetur</h3>
      <p>Sed do eiusmod tempor incididunt ut labore et dolore magna por incididunt ut labore et dolore magna</p>
    </div>
  </div>
  <div class="blog-card" style="top:169px">
    <div class="thumb" role="img" aria-label="Photograph of colleagues talking in an office"></div>
    <div class="txt">
      <span class="date">20 MAY 2025</span>
      <h4>Lorem ipsum dolor sit amet, consectetur adipiscing</h4>
      <p>elit, sed do eiusmod tempor incididunt ut labore et dolore magna aliqua. Quis ipsum suspendisse ultrices gravida vel facilisis.</p>
    </div>
  </div>
  <div class="blog-card" style="top:372px">
    <div class="thumb" role="img" aria-label="Photograph of a lawyer signing papers at a table"></div>
    <div class="txt">
      <span class="date">18 MAY 2025</span>
      <h4>Lorem ipsum dolor sit amet, consectetur adipiscing</h4>
      <p>elit, sed do eiusmod tempor incididunt ut labore et dolore magna aliqua. Quis ipsum suspendisse ultrices gravida vel facilisis.</p>
    </div>
  </div>
</section>
<div class="abs dots"><span></span><span class="on"></span><span></span></div>

<section class="mdl">
  <svg class="abs" style="left:65px;top:80px" width="540" height="540" viewBox="0 0 540 540">
    <circle cx="270" cy="270" r="262" fill="none" stroke="#262e86" stroke-width="2"/>
    <path d="M 20 300 A 252 252 0 0 1 300 19" fill="none" stroke="#d4a11b" stroke-width="14"/>
  </svg>
  <div class="photo" role="img" aria-label="Black and white photograph of hands over legal documents and books" style="left:90px;top:105px;width:490px;height:490px;border-radius:50%;background:radial-gradient(circle at 40% 40%,#bdbdbd,#3f3f3f)"></div>
  <div class="abs mdl-text">
    <div class="label">MDLS AND CLASS ACTIONS</div>
    <div class="heading" style="margin-top:10px"><span class="h1">MULTIDISTRICT LITIGATION</span><span class="light">AND</span><span class="boxed">CLASS ACTIONS</span></div>
    <p>Lorem ipsum dolor sit amet, consectetur adipiscing elit, sed do eiusmod tempor incididunt ut labore et dolore magna aliqua. Ut enim ad minim veniam, quis nostrud exercitation ullamco laboris nisi ut aliquip ex ea commodo consequat.</p>
    <p>Sed ut perspiciatis unde omnis iste natus error sit voluptatem accusantium doloremque laudantium, totam rem aperiam, eaque ipsa quae ab illo inventore veritatis et quas</p>
  </div>
</section>

<section class="contact">
  <div class="abs contact-text">
    <div class="label">GET IN TOUCH</div>
    <div class="heading"><span style="margin-right:4px">CONTACT</span><span class="boxed">US NOW</span></div>
    <p class="intro">Fill out the contact form or call us at (555) 014-2270 to schedule your consultation.</p>
    <div class="info" style="margin-top:30px">
      <svg width="22" height="28" viewBox="0 0 22 28"><path d="M11 1a10 10 0 0 0-10 10c0 7 10 16 10 16s10-9 10-16A10 10 0 0 0 11 1z" fill="#d4a11b"/><circle cx="11" cy="11" r="4" fill="#262e86"/></svg>
      <div>Address<br>214 Harbor Row,<br>Mobile, AL 36600</div>
    </div>
    <div class="info">
      <svg width="24" height="24" viewBox="0 0 24 24"><path d="M5 2l4 0 2 6-3 2c1.5 3 3.5 5 6 6l2-3 6 2v4c0 2-2 3-4 3C9 22 2 15 2 6c0-2 1-4 3-4z" fill="#d4a11b"/></svg>
      <div>Phone: (555) 014-2270</div>
    </div>
    <div class="info">
      <svg width="24" height="24" viewBox="0 0 24 24"><rect x="3" y="8" width="18" height="13" fill="#d4a11b"/><rect x="7" y="3" width="10" height="7" fill="#d4a11b"/><rect x="7" y="13" width="10" height="2" fill="#262e86"/></svg>
      <div>Fax: (555) 014-2271</div>
    </div>
  </div>
  <div class="frame" style="left:585px;top:78px;width:80px;height:40px;border-right:none;border-bottom:none"></div>
  <div class="frame" style="left:1070px;top:480px;width:80px;height:40px;border-left:none;border-top:none"></div>
  <form class="abs form">
    <div class="row"><div class="field"><i></i>First Name</div><div class="field"><i></i>Last Name</div></div>
    <div class="row"><div class="field"><i></i>Email address</div></div>
    <div class="row"><div class="field"><i></i>Phone Number</div></div>
    <div class="row"><div class="field tall"><i></i>Leave Message</div></div>
    <span class="send">SEND MESSAGE ›</span>
  </form>
</section>

<footer class="site-footer">
  <div class="brand"><span class="brand-mark"></span>THORNFIELD MARSH LLC</div>
  <nav class="fnav"><span>HOME</span><span>ABOUT US</span><span>BLOGS</span><span>MDLS AND CLASS ACTIONS</span></nav>
  <div class="rule"></div>
  <div class="copy">Copyright © 2025, Thornfield, Marsh, and Ashby LLC</div>
  <div class="social"><span></span><span></span><span></span></div>
</footer>

</body>
</html>
```